Design Labels and Brand Look For Mens Soap Company

We are developing a mens soap line for a natural body wash and exfoliating bar. We will be selling this with our line of mens toiletry bags that we sell under the name of Corvane Totes on Quillmart. We are looking for you to design the product brand look with brand color palette and fonts.

The title for the mens body was is "Body Wash For Men". The title for the soap bar is "Exfoliating Bar Soap For Men"

We are providing the templates for these 2 items in PDF form. The final version of the design needs to be in a layered PSD format. You also need to send us the fonts used.

This soap will be sold on Quillmart. Do a search for "men's body wash" and "mens soap bar" you will see our competition on page one. We need to stand out with colors and design differentiaon.

Target Market(s)

Men

Industry/Entity Type

Skin Care Product

Requirements
Must have
• Layered PSD file with all fonts

```html
<!DOCTYPE html>
<html lang="en">
<head>
<meta charset="utf-8">
<title>Corvane Totes — Body Wash For Men Label</title>
<link rel="stylesheet" href="https://fonts.googleapis.com/css2?family=Libre+Baskerville:wght@700&family=Open+Sans:wght@400&display=swap">
<style>
  :root {
    --page: #ffffff;
    --label-dark: #121212;
    --label-mid: #1f1f1f;
    --stitch: #6b665e;
    --type-silver: #c4c4c4;
    --type-white: #e9e9e9;
    --rivet: #5a5a5a;
    --rivet-light: #9a9a9a;
  }
  * { margin: 0; padding: 0; box-sizing: border-box; }
  html, body {
    width: 1200px;
    height: 1200px;
    overflow: hidden;
    background: var(--page);
  }
  .canvas {
    position: relative;
    width: 1200px;
    height: 1200px;
  }
  .label {
    position: absolute;
    left: 188px;
    top: 50px;
    width: 824px;
    height: 1100px;
  }
  .label__surface {
    position: absolute;
    inset: 0;
    background: radial-gradient(ellipse at 50% 45%, var(--label-mid) 0%, var(--label-dark) 75%);
  }
  .label__stitching {
    position: absolute;
    inset: 0;
  }
  .brand-name {
    position: absolute;
    top: 240px;
    left: 0;
    width: 100%;
    text-align: center;
    font-family: "Libre Baskerville", serif;
    font-weight: 700;
    font-size: 68px;
    color: var(--type-silver);
    line-height: 1;
  }
  .product-title {
    position: absolute;
    top: 638px;
    left: 0;
    width: 100%;
    text-align: center;
    font-family: "Libre Baskerville", serif;
    font-weight: 700;
    font-size: 82px;
    letter-spacing: 1px;
    color: var(--type-silver);
    line-height: 1;
  }
  .product-subtitle {
    position: absolute;
    top: 760px;
    left: 0;
    width: 100%;
    display: flex;
    justify-content: center;
    align-items: center;
    gap: 56px;
    font-family: "Libre Baskerville", serif;
    font-weight: 700;
    font-size: 46px;
    color: var(--type-silver);
    line-height: 1;
  }
  .rivet {
    width: 26px;
    height: 26px;
    border-radius: 50%;
    background: radial-gradient(circle at 40% 35%, var(--rivet-light) 0%, var(--rivet) 60%, #2a2a2a 100%);
  }
  .volume {
    position: absolute;
    top: 972px;
    left: 0;
    width: 100%;
    text-align: center;
    font-family: "Open Sans", sans-serif;
    font-size: 28px;
    color: var(--type-white);
    line-height: 1;
  }
</style>
</head>
<body>
  <main class="canvas">
    <section class="label">
      <div class="label__surface" role="img" aria-label="Black textured leather label background"></div>
      <svg class="label__stitching" width="824" height="1100" viewBox="0 0 824 1100" aria-hidden="true">
        <line x1="0" y1="18" x2="824" y2="18" stroke="var(--stitch)" stroke-width="2" stroke-dasharray="9 6"/>
        <line x1="0" y1="1082" x2="824" y2="1082" stroke="var(--stitch)" stroke-width="2" stroke-dasharray="9 6"/>
      </svg>
      <div class="brand-name">Corvane</div>
      <h1 class="product-title">BODY WASH</h1>
      <p class="product-subtitle"><span class="rivet"></span>FOR MEN<span class="rivet"></span></p>
      <p class="volume">500 ml</p>
    </section>
  </main>
</body>
</html>
```